Honey Label for a private beekeeper

I am an "amateur" beekeeper and like to promote and sell my honey. The target group is anyone who likes honey. Task: The label design should basically be an "eye-catcher" and express the high quality of the natural product honey. In the narrower sense, but which should form a unit in the design: The first part is the so-called guaranty; he connects with the glass and tears when first opening the lid. The lock should be about 2 inches wide and 8 inches long, and adorned by the words 'The best of the nature'. In brackets you always find the english translation of the german text for a better understanding. The second part is the product label. For this there are no shape specifications but max. height is 5cm and maximum is 12cm (for 500g jar), but the following must be included in the account: "Please use the following placeholders", "first name last name", "street house number", "post code city name ") as well as the words" 500g "," Best Before Date ", (" Best before "), behind or below please leave blank space for the stamp imprint of the date," Store dry, dark and protected from heat! dry, dark and protected from heat), And - most important - the text: "Finest bee honey" and in new line "from Cologne - Porz (from Cologne - Porz)" as well as the two varieties "Summer Blossom" or "Spring Blossom" ... in the future may be added more varieties. The company logo should be used in a single color, so that the customer can quickly identify the type of honey in the glass. For this purpose, the respective honeysuckle color, in whatever form, dominate the label or a certain area of ​​it. I have uploaded a few labels from the internet that appealed to me about their style, but it's definitely not about making just one copy of one of these labels. Please use the german text on the label, the translation is just for you. Please contact me in case of any further questions or problems with my explanation. I'm looking forward to your designs! As an 'amateur' I run a hobby-beekeeping and want to drive out my evening gown and summer turkey honey. The target group is anyone who likes honey. Task The Etiketten_Design to be designed should basically be an "eye-catcher", have a high recognition value and express the high quality of the natural product honey. In the narrower sense, two independent parts of the label are to be designed, but which should form a unit in the design: The first part is the so-called warranty; he connects the lid with the glass and tears when first opening the lid. The lock should be about 2 cm wide and 8 cm long, and adorned by the saying 'the best of nature'. The second part is the actual product label. For this there are no size and shape specifications, but the following contents must be considered: The data of the beekeeper (please use the following placeholders "first name last name", "street house number", "ZIP place name") and the information "500g", "At least Best before: "(behind or below, please leave white space for the stamp imprint of the date)," dry, dark and protect from heat! ", and - most importantly - the text: finest bee honey (new line) from Cologne - Porz as well the two denominations spring blossom or summer bloom (in the future may be added more varieties). The logo of the company should be used, but it can also be used on the freshly-baked seal (see appendix) Each type of honey (summer blossom and spring blossom) should be associated with a color, so that the customer can quickly identify which type of honey is in the glass. For this, the respective honeysuckle color, in whatever form, should dominate the label or a certain area of ​​it. With regard to a good reproducibility of the labels in large quantities, we ask for the following further requirements to be observed: • Please place text and picture elements with 4mm distance to the label edges. • Please consider the CYMK color scheme. • If you choose multicolored labels, please use a maximum of four colors. • The honeysuckle color of the product label should NOT be found on the warranty seal (because the guarantee applies generally to any honey jar, regardless of the honeys). • The product label should be editable. • The product label should be scalable (for both small 250g glasses and large 500g glasses). The last two points can be ignored if a larger copy with the indication "500g" and a smaller one with the indication "250g" are created per product label. I'm looking forward to your designs!

Target Market(s)

Neighborhood and shops

Colors

Designer to choose colors to be used in the design.

Requirements
Must have
• With regard to the following further requirements: • Please place text and picture elements 4mm from the edges of the labels. • Please consider the CYMK color scheme. • If you choose multicolored labels, please use a maximum of four colors. The honeysuckle color of the product label should not be found on the warranty. • The product label should be editable. • The product label needs to be scalable The "500g" and the smaller "250g" are created by product label.
Should not have
• Please do not use the color gold no transparent labels

```html
<!DOCTYPE html>
<html lang="de">
<head>
<meta charset="utf-8">
<title>Feinster Bienenhonig – Etiketten</title>
<link rel="stylesheet" href="https://fonts.googleapis.com/css2?family=Dancing+Script:wght@500&family=Montserrat:wght@400;700&display=swap">
<style>
  :root {
    --paper: #ffffff;
    --ink: #3d3d3d;
    --spring-tint: #cfe3d9;
    --spring-deep: #a9cbbc;
    --spring-tag: #7fa597;
    --summer-tint: #f6e1bb;
    --summer-deep: #efc88a;
    --summer-tag: #c9302c;
    --summer-accent: #e8823a;
    --generic-tint: #d3e8ec;
    --generic-deep: #aed2d9;
    --generic-tag: #4f7f8b;
    --seal-mark: #b5b5b5;
    --shadow: rgba(0,0,0,0.08);
  }
  * { margin: 0; padding: 0; box-sizing: border-box; }
  html, body { width: 1200px; height: 1200px; overflow: hidden; background: var(--paper); }
  body { position: relative; font-family: "Montserrat", sans-serif; color: var(--ink); }

  .product { position: absolute; top: 375px; width: 305px; height: 320px; }
  .product--spring { left: 95px; }
  .product--summer { left: 445px; }
  .product--generic { left: 795px; }

  .seal {
    position: absolute; left: 157px; top: 0; width: 38px; height: 93px;
    background: var(--paper); box-shadow: 0 0 4px var(--shadow);
  }
  .seal svg { position: absolute; left: 12px; bottom: 12px; }

  .label {
    position: absolute; left: 0; top: 130px; width: 305px; height: 185px;
    background: var(--paper); box-shadow: 0 1px 6px var(--shadow); overflow: hidden;
  }
  .label__pattern { position: absolute; left: 22px; right: 0; top: 35px; bottom: 0; }
  .product--spring .label__pattern { background: linear-gradient(180deg, rgba(207,227,217,0) 0%, var(--spring-tint) 30%, var(--spring-deep) 100%); }
  .product--summer .label__pattern { background: linear-gradient(180deg, rgba(246,225,187,0) 0%, var(--summer-tint) 30%, var(--summer-deep) 100%); }
  .product--generic .label__pattern { background: linear-gradient(180deg, rgba(211,232,236,0) 0%, var(--generic-tint) 30%, var(--generic-deep) 100%); }

  .label__side {
    position: absolute; left: 1px; top: 84px; width: 20px;
    font-size: 4px; line-height: 6px; color: var(--ink); white-space: nowrap;
  }
  .label__side-bar { display: block; width: 20px; height: 20px; margin-top: 6px; }
  .product--spring .label__side-bar { background: var(--spring-tag); opacity: .5; }
  .product--summer .label__side-bar { background: var(--summer-accent); opacity: .7; }
  .product--generic .label__side-bar { background: var(--generic-tag); opacity: .4; }

  .label__title {
    position: absolute; left: 0; right: 0; top: 20px; text-align: center;
    font-family: "Dancing Script", cursive; font-weight: 500; font-size: 25px; color: #4a4a4a;
  }
  .label__origin {
    position: absolute; left: 0; right: 0; top: 56px; text-align: center;
    font-size: 11px; letter-spacing: 1.6px; color: #555;
  }
  .label__variety {
    position: absolute; left: 50%; top: 136px; transform: translateX(-50%);
    padding: 2px 8px; font-size: 11.5px; font-weight: 700; letter-spacing: 1.6px; color: var(--paper); white-space: nowrap;
  }
  .product--spring .label__variety { background: var(--spring-tag); }
  .product--summer .label__variety { background: var(--summer-tag); }
  .product--generic .label__variety { background: var(--generic-tag); }
  .label__weight {
    position: absolute; left: 0; right: 0; top: 160px; text-align: center;
    font-size: 11.5px; font-weight: 700; color: #333;
  }
</style>
</head>
<body>
  <section class="product product--spring">
    <div class="seal"><svg width="14" height="14" viewBox="0 0 14 14"><polygon points="7,1 12.5,4 12.5,10 7,13 1.5,10 1.5,4" fill="none" stroke="var(--seal-mark)" stroke-width="1"/></svg></div>
    <div class="label">
      <div class="label__pattern" role="img" aria-label="Wabenmuster in Frühlingsgrün"></div>
      <div class="label__side">Vorname<br>Weg 12<br>PLZ Ort<span class="label__side-bar"></span></div>
      <p class="label__title">Feinster Bienenhonig</p>
      <p class="label__origin">AUS LINDENHAIN</p>
      <p class="label__variety">FRÜHLINGSBLÜTE</p>
      <p class="label__weight">500g</p>
    </div>
  </section>

  <section class="product product--summer">
    <div class="seal"><svg width="14" height="14" viewBox="0 0 14 14"><polygon points="7,1 12.5,4 12.5,10 7,13 1.5,10 1.5,4" fill="none" stroke="var(--seal-mark)" stroke-width="1"/></svg></div>
    <div class="label">
      <div class="label__pattern" role="img" aria-label="Wabenmuster in Sommergelb und Orange"></div>
      <div class="label__side">Vorname<br>Weg 12<br>PLZ Ort<span class="label__side-bar"></span></div>
      <p class="label__title">Feinster Bienenhonig</p>
      <p class="label__origin">AUS LINDENHAIN</p>
      <p class="label__variety">SOMMERBLÜTE</p>
      <p class="label__weight">500g</p>
    </div>
  </section>

  <section class="product product--generic">
    <div class="seal"><svg width="14" height="14" viewBox="0 0 14 14"><polygon points="7,1 12.5,4 12.5,10 7,13 1.5,10 1.5,4" fill="none" stroke="var(--seal-mark)" stroke-width="1"/></svg></div>
    <div class="label">
      <div class="label__pattern" role="img" aria-label="Wabenmuster in Hellblau"></div>
      <div class="label__side">Vorname<br>Weg 12<br>PLZ Ort<span class="label__side-bar"></span></div>
      <p class="label__title">Feinster Bienenhonig</p>
      <p class="label__origin">AUS LINDENHAIN</p>
      <p class="label__variety">PLATZHALTER</p>
      <p class="label__weight">500g</p>
    </div>
  </section>
</body>
</html>
```